Small rum distillery looking for bottle design

Small rum distillery in Estonia. Looking for bottle lable design. It should be simple but at the same time point out from the variety of other bottles.
As we are a small nordic country, design can be some how nordic or represent our country. It can also have some connection with sailing or sea as we know it pirates love it.
Bottle we are using is Brisela 500

Industry/Entity Type

food and beverage

Other font styles liked:
• Baskerville

```html
<!DOCTYPE html>
<html lang="en">
<head>
<meta charset="utf-8">
<title>Seafrost Premium Estonian Rum – Label</title>
<link rel="stylesheet" href="https://fonts.googleapis.com/css2?family=Libre+Baskerville:wght@400;700&family=Playfair+Display:wght@900&display=swap">
<style>
  :root {
    --paper: #f8f6f2;
    --ink: #16130f;
    --ink-soft: #3a3530;
    --gold: #c69a3a;
    --gold-dark: #8f6a1f;
    --amber: #e8651c;
    --amber-light: #f39a55;
    --sketch-light: #e7e4de;
    --sketch-mid: #b9b4ab;
    --page: #ffffff;
  }
  * { box-sizing: border-box; margin: 0; padding: 0; }
  html, body {
    width: 1200px; height: 1200px; overflow: hidden;
    background: var(--page);
  }
  .canvas {
    position: relative; width: 1200px; height: 1200px;
    font-family: "Libre Baskerville", Georgia, serif;
    color: var(--ink);
  }

  /* Front label */
  .front-label {
    position: absolute; left: 270px; top: 90px;
    width: 660px; height: 640px;
    background: var(--paper);
    border-left: 10px solid var(--amber);
    border-right: 10px solid var(--amber);
    display: flex; flex-direction: column; align-items: center;
  }
  .gold-band {
    position: absolute; left: 0; right: 0; height: 16px;
    border-top: 3px solid var(--gold);
    border-bottom: 3px solid var(--gold);
    background: linear-gradient(var(--paper), var(--paper)) padding-box;
  }
  .gold-band::after {
    content: ""; position: absolute; left: 0; right: 0; top: 4px; height: 2px;
    background: var(--gold-dark); opacity: .6;
  }
  .gold-band--top { top: 14px; }
  .gold-band--bottom { bottom: 14px; }

  .brand {
    margin-top: 58px;
    display: flex; flex-direction: column; align-items: center;
  }
  .brand-dot {
    width: 34px; height: 34px; border-radius: 50%;
    background: var(--gold);
    margin-bottom: 8px;
  }
  .brand-name {
    font-size: 32px; font-weight: 400; letter-spacing: 2px; color: var(--ink);
    line-height: 1;
  }
  .brand-sub {
    font-size: 10px; letter-spacing: 6px; color: var(--ink);
    margin-top: 6px; padding-top: 4px;
    border-top: 1px solid var(--gold);
  }

  .ship-art {
    width: 440px; height: 200px; margin-top: 8px;
    border-radius: 50% 50% 40% 40%;
    background: radial-gradient(ellipse at 50% 55%, #2a2622 0 12%, var(--sketch-mid) 26%, var(--sketch-light) 52%, var(--paper) 72%);
  }

  .product-name {
    font-family: "Playfair Display", "Libre Baskerville", serif;
    font-weight: 900; font-size: 94px; line-height: 1;
    letter-spacing: 1px; margin-top: -14px; color: var(--ink);
  }
  .product-descriptor {
    font-size: 24px; letter-spacing: 1px; color: var(--ink-soft);
    margin-top: 8px;
  }
  .product-type {
    font-size: 68px; letter-spacing: 3px; line-height: 1; margin-top: 10px;
  }
  .origin {
    font-size: 10px; font-weight: 700; letter-spacing: .5px; margin-top: 12px;
  }

  /* Batch label */
  .batch-label {
    position: absolute; left: 330px; top: 780px;
    width: 540px; height: 190px;
    background: var(--paper);
    border-left: 6px solid var(--amber);
    border-right: 6px solid var(--amber);
    display: flex; align-items: stretch;
    padding: 18px 0;
  }
  .batch-side {
    width: 56px; display: flex; align-items: center; justify-content: center;
  }
  .batch-side span {
    font-size: 24px; letter-spacing: 1px; white-space: nowrap;
  }
  .batch-side--left span { transform: rotate(-90deg); }
  .batch-side--right span { transform: rotate(90deg); }

  .batch-table {
    flex: 1; border: 1.5px solid var(--ink);
    display: grid;
    grid-template-columns: 96px 1fr 1fr;
    grid-template-rows: 1fr 38px 1fr;
  }
  .batch-cell {
    display: flex; align-items: center; justify-content: center; text-align: center;
  }
  .batch-claim {
    grid-column: 1 / 4; font-size: 13px; letter-spacing: 1.5px; line-height: 1.6;
    border-bottom: 1.5px solid var(--ink); padding: 0 10px;
  }
  .batch-number {
    grid-row: 2 / 4; grid-column: 1; flex-direction: column;
    font-size: 24px; line-height: 1.3; border-right: 1.5px solid var(--ink);
  }
  .batch-spirit {
    grid-column: 2 / 4; font-size: 11px; font-weight: 700; letter-spacing: 3.5px;
    border-bottom: 1.5px solid var(--ink);
  }
  .batch-volume { font-size: 18px; border-right: 1.5px solid var(--ink); margin: 10px 0; }
  .batch-abv { font-size: 18px; }
</style>
</head>
<body>
<main class="canvas">
  <section class="front-label">
    <div class="gold-band gold-band--top"></div>

    <header class="brand">
      <div class="brand-dot"></div>
      <div class="brand-name">HALLIK</div>
      <div class="brand-sub">DISTILLERY</div>
    </header>

    <div class="ship-art" role="img" aria-label="Engraved illustration of a tall sailing ship on waves with billowing sails"></div>

    <h1 class="product-name">SEAFROST</h1>
    <p class="product-descriptor">PREMIUM ESTONIAN</p>
    <p class="product-type">RUM</p>
    <p class="origin">PRODUCT OF ESTONIA</p>

    <div class="gold-band gold-band--bottom"></div>
  </section>

  <section class="batch-label">
    <div class="batch-side batch-side--left"><span>SMALL</span></div>
    <div class="batch-table">
      <div class="batch-cell batch-claim">HAND CRAFTED IN ESTONIA WITH ONLY<br>THE HIGHEST QUALITY INGREDIENTS</div>
      <div class="batch-cell batch-number"><span>NO.</span><span>001</span></div>
      <div class="batch-cell batch-spirit">PREMIUM DISTILLED SPIRIT</div>
      <div class="batch-cell batch-volume">700 ML</div>
      <div class="batch-cell batch-abv">45% ALC/ VOL</div>
    </div>
    <div class="batch-side batch-side--right"><span>BATCH</span></div>
  </section>
</main>
</body>
</html>
```